Business Card & Stationary Design Project

We are looking for some creative direction for business cards and our stationary.

We are a global logistics firm that has recently changed its name to Marrick Global Logistics and we have a new website due out tomorrow (www.marrick.com.au).

The colours of the company are rich navy tones, I would like to have business cards that fit together to make one picture on the back (possibly an old map of the world??), and the front to be modern contemporary looking.

But I am open to suggestions, so just incorporate our new logo and get going!
Updates

Hi Everyone,

Thank you for all of your designs so far and the time you have put into it.

I have asked many of you for amendments to see if we can get a final product, so with this in mind I am extending the deadline by a few days.

Good luck and thank you once again.

Please message me direct if you need any clarification.

Kind Regards
Colin

Reason: As outlined the extra 3 days is for amendments and changes to the current submissions. Thanks Colin

Industry/Entity Type

Business

```html
<!DOCTYPE html>
<html lang="en">
<head>
<meta charset="utf-8">
<title>Marrick Global Logistics – Business Card</title>
<link rel="stylesheet" href="https://fonts.googleapis.com/css2?family=Cinzel:wght@600&family=Source+Sans+3:wght@400;700&display=swap">
<style>
  :root {
    --stage: #2b2b2d;
    --navy: #1f1f5e;
    --steel-deep: #3f5f96;
    --steel-mid: #8da3cc;
    --steel-light: #e4e8f3;
    --parchment-light: #f1c58f;
    --parchment: #e2a466;
    --parchment-deep: #b7652f;
    --land: #8a3415;
    --contact-text: #ffffff;
  }
  * { margin: 0; padding: 0; box-sizing: border-box; }
  html, body {
    width: 1200px;
    height: 1000px;
    overflow: hidden;
    background: var(--stage);
  }
  .canvas {
    position: relative;
    width: 1200px;
    height: 1000px;
  }
  .card {
    position: absolute;
    left: 219px;
    width: 710px;
    box-shadow: 0 6px 18px rgba(0, 0, 0, 0.45);
    overflow: hidden;
  }
  .card-front {
    top: 66px;
    height: 405px;
    background:
      repeating-linear-gradient(90deg, rgba(255,255,255,0.08) 0 1px, rgba(0,0,0,0) 1px 3px, rgba(40,60,110,0.07) 3px 4px, rgba(0,0,0,0) 4px 7px),
      linear-gradient(180deg, var(--steel-deep) 0%, var(--steel-mid) 22%, var(--steel-light) 45%, var(--steel-light) 55%, var(--steel-mid) 78%, var(--steel-deep) 100%);
  }
  .logo-band {
    position: absolute;
    left: 150px;
    right: 150px;
    top: 119px;
    height: 153px;
    background: rgba(255, 255, 255, 0.18);
  }
  .wordmark {
    position: absolute;
    left: 0;
    right: 0;
    top: 160px;
    text-align: center;
    color: var(--navy);
    font-family: "Cinzel", serif;
    font-weight: 600;
  }
  .wordmark-name {
    display: block;
    font-size: 50px;
    line-height: 1;
    letter-spacing: 0.42em;
    padding-left: 0.42em;
  }
  .wordmark-tagline {
    display: block;
    margin-top: 8px;
    font-size: 20px;
    letter-spacing: 0.32em;
    padding-left: 0.32em;
  }
  .card-back {
    top: 528px;
    height: 405px;
  }
  .world-map {
    position: absolute;
    inset: 0;
    background:
      radial-gradient(ellipse 30% 35% at 35% 28%, var(--land) 0%, rgba(138,52,21,0) 100%),
      radial-gradient(ellipse 20% 40% at 90% 45%, var(--land) 0%, rgba(138,52,21,0) 100%),
      radial-gradient(ellipse 60% 60% at 60% 60%, var(--parchment-light) 0%, var(--parchment) 60%, var(--parchment-deep) 100%);
  }
  .contact-list {
    position: absolute;
    left: 34px;
    bottom: 18px;
    list-style: none;
    font-family: "Source Sans 3", sans-serif;
    font-size: 14.5px;
    line-height: 22.5px;
    color: var(--contact-text);
    text-shadow: 0 1px 2px rgba(60, 20, 0, 0.5);
  }
  .contact-label { font-weight: 700; }
</style>
</head>
<body>
<main class="canvas">
  <section class="card card-front" aria-label="Card front">
    <div class="logo-band"></div>
    <h1 class="wordmark">
      <span class="wordmark-name">MARRICK</span>
      <span class="wordmark-tagline">GLOBAL LOGISTICS</span>
    </h1>
  </section>

  <section class="card card-back" aria-label="Card back">
    <div class="world-map" role="img" aria-label="Antique-style world map in rust and parchment tones, Pacific-centred"></div>
    <ul class="contact-list">
      <li><span class="contact-label">Phone:</span> 02 9471 2860</li>
      <li><span class="contact-label">Mobile:</span> 0412587316</li>
      <li><span class="contact-label">Fax:</span> 029471 2861</li>
      <li><span class="contact-label">Email:</span> colin@marrick.com.au</li>
      <li><span class="contact-label">Web:</span> marrick.com.au</li>
      <li><span class="contact-label">Address:</span> 58 Harbour Lane Pyrmont NSW 2009</li>
    </ul>
  </section>
</main>
</body>
</html>
```